VORLEN Website Design

We need a website designed for our company VORLEN. We are a luxury lifestyle club that will provide benefits and services for our members. The site should be clean & sleek, preferably using black and white (or darker colors). (example sites: brimvale.example, tusko.example)

Here is a link of a sample page I did using wix. (https://pelmundry4.sitebuild.example/mypage) This can be used to get a general idea.

Target Market(s)

Upper Middle Class in the United States

Number of Pages Required

5+ page

Font styles to use
Sans Serif
Other font styles liked:
• Arial (or other similar fonts)

Requirements
Must have
• A clean design that is eye-catching and speaks to our company.
Nice to have
• Ideas for copy.

```html
<!DOCTYPE html>
<html lang="en">
<head>
<meta charset="utf-8">
<title>VORLEN — A Members Only Lifestyle Club</title>
<link href="https://fonts.googleapis.com/css2?family=Montserrat:wght@300;400;500;600;700&family=Open+Sans:wght@400;600&display=swap" rel="stylesheet">
<style>
:root{
  --ink:#000;
  --paper:#fff;
  --charcoal:#1a1a1a;
  --muted:#6b6b6b;
  --rule:#c9c9c9;
  --field:#f1f1f1;
  --hero-a:#2a1410;
  --hero-b:#7a3a22;
  --hero-c:#c98a4a;
  --band-a:#3b3430;
  --band-b:#5e544c;
  --foot-a:#1c1330;
  --foot-b:#3b2350;
}
*{box-sizing:border-box;margin:0;padding:0}
html,body{width:1200px;height:4972px;overflow:hidden}
body{font-family:"Open Sans",Arial,sans-serif;color:var(--ink);background:var(--paper);position:relative}
h1,h2,h3,h4,.brand,.nav a,.btn{font-family:"Montserrat",Arial,sans-serif}
section,header,footer{position:absolute;left:0;width:1200px}
.center{text-align:center}
.title{font-weight:400;font-size:30px;letter-spacing:.5px}
.title::after{content:"";display:block;width:50px;height:2px;background:currentColor;margin:16px auto 0}
.btn{display:inline-block;font-size:13px;font-weight:500;padding:0 28px;height:30px;line-height:30px;text-decoration:none}
.btn-dark{background:var(--ink);color:var(--paper)}
.btn-light{background:var(--paper);color:var(--ink)}

/* header */
.site-header{top:0;height:126px;background:var(--ink);color:var(--paper)}
.brand{position:absolute;left:83px;top:34px;font-size:44px;font-weight:400;letter-spacing:1px;color:var(--paper)}
.nav{position:absolute;left:480px;top:46px;display:flex;gap:16px;align-items:center;white-space:nowrap}
.nav a{color:var(--paper);font-size:13px;text-decoration:none;padding:3px 10px;line-height:18px}
.nav a.active{border:1px solid var(--paper);border-radius:12px}
.social{position:absolute;left:1010px;top:52px;display:flex;gap:10px}
.social span{width:13px;height:13px;border-radius:50%;background:var(--paper)}

/* hero */
.hero{top:126px;height:729px;color:var(--paper)}
.hero-photo{position:absolute;inset:0;background:linear-gradient(120deg,var(--hero-a) 0%,var(--hero-b) 40%,var(--hero-c) 60%,var(--hero-a) 100%)}
.hero-shade{position:absolute;inset:0;background:rgba(0,0,0,.25)}
.hero h1{position:absolute;top:372px;width:100%;text-align:center;font-size:46px;font-weight:500}
.hero-actions{position:absolute;top:470px;width:100%;display:flex;justify-content:center;gap:6px}
.hero-actions .btn{height:44px;line-height:44px;font-size:18px;padding:0 40px}
.dots{position:absolute;top:610px;width:100%;display:flex;justify-content:center;gap:8px}
.dots span{width:9px;height:9px;border-radius:50%;border:1px solid var(--paper)}
.dots span.on{background:var(--paper)}

/* about */
.about{top:855px;height:481px}
.about h2{position:absolute;top:108px;width:100%}
.about h2 b{font-weight:700}
.about h3{position:absolute;top:202px;width:100%;font-size:14px;font-weight:700}
.about p{position:absolute;top:238px;left:280px;width:640px;font-size:11.5px;line-height:22px;color:var(--muted);text-align:center}
.about .btn{position:absolute;top:366px;left:540px;width:120px;height:26px;line-height:26px;text-align:center;padding:0}

/* services */
.services{top:1336px;height:772px;color:var(--paper)}
.band-photo{position:absolute;inset:0;background:linear-gradient(160deg,var(--band-a),var(--band-b) 50%,var(--band-a))}
.band-shade{position:absolute;inset:0;background:rgba(0,0,0,.35)}
.services h2{position:absolute;top:104px;width:100%}
.services p.lead{position:absolute;top:188px;left:230px;width:740px;font-size:11.5px;line-height:19px;text-align:center}
.cards{position:absolute;top:308px;left:126px;display:flex;gap:30px}
.card{width:298px;height:250px;background:var(--paper);color:var(--ink);padding:6px;text-align:center}
.card .photo{height:185px}
.card h4{font-size:16px;font-weight:700;margin-top:10px}
.card p{font-size:10.5px;line-height:14px;color:var(--muted);margin:4px 16px 0}
.services .btn{position:absolute;top:672px;left:542px;width:116px;height:30px;padding:0;text-align:center;font-size:12px}

/* apply */
.apply{top:2108px;height:521px;background:var(--ink);color:var(--paper)}
.apply h2{position:absolute;top:90px;width:100%;font-size:30px;font-weight:400}
.apply p{position:absolute;top:160px;width:100%;font-size:12px;line-height:20px}
.apply h3{position:absolute;top:240px;width:100%;font-size:22px;font-weight:400}
.fields{position:absolute;top:318px;left:172px;display:flex;gap:13px}
.field{height:40px;background:var(--paper);color:#999;font-size:12px;padding:11px 8px}
.apply .btn{position:absolute;top:404px;left:540px;width:120px;height:30px;padding:0;text-align:center}

/* experience */
.experience{top:2629px;height:593px}
.experience h2{position:absolute;top:90px;width:100%}
.experience .photo{position:absolute;top:202px;left:182px;width:382px;height:252px;background:linear-gradient(135deg,#2a1a5a,#6a3aa8 45%,#1e8fc9 70%,#120d2a)}
.experience .copy{position:absolute;top:206px;left:627px;width:360px;font-size:12px;line-height:20px;color:var(--muted)}
.experience .copy p{margin-bottom:18px}
.experience .btn{position:absolute;top:434px;left:627px;width:118px;height:28px;line-height:28px;padding:0;text-align:center;font-size:12px}

/* contact */
.contact{top:3222px;height:660px}
.contact .band{position:absolute;top:0;left:0;width:1200px;height:557px;color:var(--paper)}
.contact .band-photo{background:linear-gradient(150deg,#2b1d14,#5a4230 50%,#2b1d14)}
.contact h2{position:absolute;top:96px;width:100%;color:var(--paper);font-size:30px;font-weight:400}
.contact-form{position:absolute;top:209px;left:225px;width:746px;height:424px;background:var(--paper);box-shadow:0 4px 14px rgba(0,0,0,.25);padding:34px 40px}
.contact-form label{display:block;font-size:12px;color:#444;margin-bottom:6px}
.row{display:flex;gap:24px}
.row>div{flex:1}
.box{background:var(--field);border:1px solid var(--rule);height:38px;margin-bottom:16px}
.box.tall{height:108px}
.contact-form .btn{position:absolute;left:328px;bottom:34px;width:90px;height:26px;line-height:26px;padding:0;text-align:center;font-size:12px}

/* testimonials */
.testimonials{top:3882px;height:633px}
.testimonials h2{position:absolute;top:0;width:100%;font-size:30px;font-weight:400}
.testimonials .lead{position:absolute;top:74px;left:340px;width:520px;text-align:center;font-size:11.5px;line-height:19px;color:var(--muted)}
.people{position:absolute;top:256px;left:182px;display:flex;gap:62px}
.person{width:240px}
.avatar{width:66px;height:66px;border-radius:50%;margin:0 auto;background:linear-gradient(135deg,#c8a58a,#6e5444)}
.person h4{text-align:center;font-size:14px;font-weight:700;margin-top:14px}
.person .role{text-align:center;font-size:10px;color:var(--muted)}
.quote-mark{width:18px;height:14px;margin-top:28px}
.person p{font-size:11.5px;line-height:18px;color:#444;margin-top:6px}

/* footer */
.site-footer{top:4515px;height:457px;color:var(--paper)}
.site-footer .band-photo{background:linear-gradient(180deg,var(--foot-b),var(--foot-a) 55%,#0e0a1a)}
.site-footer .band-shade{background:rgba(0,0,0,.2)}
.foot-brand{position:absolute;left:83px;top:100px;font-family:"Montserrat",Arial,sans-serif;font-size:44px;font-weight:400}
.foot-about{position:absolute;left:83px;top:162px;width:190px;font-size:11px;line-height:15px}
.col{position:absolute;top:108px}
.col h4{font-size:16px;font-weight:500;letter-spacing:1px;margin-bottom:18px}
.col-contact{left:351px}
.info{display:flex;gap:10px;font-size:12px;line-height:16px;margin-bottom:14px}
.info svg{flex:none}
.info b{font-weight:600}
.col-about{left:620px}
.col-about a{display:block;color:var(--paper);text-decoration:none;font-size:13px;line-height:24px}
.col-touch{left:802px;width:320px}
.col-touch .row{gap:8px}
.col-touch .in{height:36px;background:var(--paper);color:#777;font-size:12px;padding:10px 8px;margin-bottom:8px}
.col-touch .btn{height:34px;line-height:34px;width:132px;padding:0;text-align:center;font-weight:700}
.copyright{position:absolute;bottom:0;left:0;width:100%;height:46px;line-height:46px;text-align:center;font-size:11px;background:rgba(0,0,0,.55)}
</style>
</head>
<body>

<header class="site-header">
  <div class="brand">VORLEN</div>
  <nav class="nav">
    <a class="active" href="#">Home</a>
    <a href="#">About</a>
    <a href="#">Services &amp; benefits</a>
    <a href="#">Apply</a>
    <a href="#">Contact</a>
  </nav>
  <div class="social"><span></span><span></span><span></span><span></span></div>
</header>

<section class="hero">
  <div class="hero-photo" role="img" aria-label="Photo of club members raising champagne glasses at a festive party"></div>
  <div class="hero-shade"></div>
  <h1>A Members Only Lifestyle Club</h1>
  <div class="hero-actions">
    <a class="btn btn-light" href="#">Join now</a>
    <a class="btn btn-dark" href="#">Visit our Club</a>
  </div>
  <div class="dots"><span class="on"></span><span></span><span></span></div>
</section>

<section class="about">
  <h2 class="title center">About <b>VORLEN</b></h2>
  <h3 class="center">The ultimate full service lifestyle club</h3>
  <p>VORLEN was formed to bring the best services, experiences, and exclusive opportunities to our members. With everything from private member events to private jet travel, the perks of being a VORLEN member are unmatched. Professional athletes, artists, musicians, corporate professionals: our members come from diverse backgrounds. Comprehensive services like 24/7 concierge, accountants, attorneys, private advisers, planners, investment advisers and more.</p>
  <a class="btn btn-dark" href="#">Apply</a>
</section>

<section class="services">
  <div class="band-photo" role="img" aria-label="Photo of members laughing together at a social gathering"></div>
  <div class="band-shade"></div>
  <h2 class="title center">Services &amp; Benefits</h2>
  <p class="lead">VORLEN membership provides you with amazing benefits and services. Members receive access to the best concierge, advisers, fine restaurants, private lounges, planners and more. VORLEN members also receive access to private travel, premium luxury experiences, private social clubs, and private investment opportunities.</p>
  <div class="cards">
    <article class="card">
      <div class="photo" role="img" aria-label="Photo of a private jet on the tarmac with a red carpet" style="background:linear-gradient(160deg,#9fb6c8,#e8e4df 55%,#8a2a22)"></div>
      <h4>Private Jet Travel</h4>
      <p>Fly on your own schedule with private departures, crews and lounges.</p>
    </article>
    <article class="card">
      <div class="photo" role="img" aria-label="Photo of an infinity pool at sunset with palm trees" style="background:linear-gradient(180deg,#e7a27a,#f2c9a0 50%,#4f7f9a)"></div>
      <h4>Experience</h4>
      <p>Curated trips, private resorts and rare moments for our members.</p>
    </article>
    <article class="card">
      <div class="photo" role="img" aria-label="Photo of a candlelit private dinner table" style="background:linear-gradient(160deg,#2a1a12,#8a5a2a 50%,#1a120c)"></div>
      <h4>Private Events</h4>
      <p>Intimate dinners, launches and members' nights, by invitation only.</p>
    </article>
  </div>
  <a class="btn btn-light" href="#">More Service</a>
</section>

<section class="apply">
  <h2 class="center">Apply For a Lifestyle Club</h2>
  <p class="center">Hey! Thanks for your interest! We will begin accepting applications in 2019.<br>In the meantime, simply fill out the indication of interest below and we will be in touch once we begin accepting applications.</p>
  <h3 class="center">Indication of Interest</h3>
  <div class="fields">
    <div class="field" style="width:279px">Name</div>
    <div class="field" style="width:275px">Email</div>
    <div class="field" style="width:276px">Phone</div>
  </div>
  <a class="btn btn-light" href="#">Submit</a>
</section>

<section class="experience">
  <h2 class="title center">Experience</h2>
  <div class="photo" role="img" aria-label="Photo of a crowded concert with stage lights"></div>
  <div class="copy">
    <p>VORLEN organizes and supports a ton of private events and parties for our members.</p>
    <p>Members are also provided access to exclusive venues and events from our partners.</p>
    <p>Network with other members to build lasting relationships.</p>
  </div>
  <a class="btn btn-dark" href="#">Learn More</a>
</section>

<section class="contact">
  <div class="band">
    <div class="band-photo" role="img" aria-label="Photo of friends toasting with drinks"></div>
    <div class="band-shade"></div>
  </div>
  <h2 class="center">We're always here, drop as a line!</h2>
  <form class="contact-form">
    <div class="row">
      <div><label>Name</label><div class="box"></div></div>
      <div><label>Email</label><div class="box"></div></div>
    </div>
    <label>Subject</label><div class="box"></div>
    <label>Message</label><div class="box tall"></div>
    <a class="btn btn-dark" href="#">Send</a>
  </form>
</section>

<section class="testimonials">
  <h2 class="title center">What our Clients Says</h2>
  <p class="lead">Our members share what the club has meant for their work, travel and time with family and friends across the country.</p>
  <div class="people">
    <div class="person">
      <div class="avatar" role="img" aria-label="Portrait photo of David"></div>
      <h4>David</h4><div class="role">Member</div>
      <svg class="quote-mark" viewBox="0 0 18 14"><path d="M0 14V8C0 3 2 0 7 0v3C4 3 3 5 3 7h4v7zM11 14V8c0-5 2-8 7-8v3c-3 0-4 2-4 4h4v7z"/></svg>
      <p>The concierge team sorted a last minute trip for my whole family. Every detail was handled before we even asked, and it felt effortless.</p>
    </div>
    <div class="person">
      <div class="avatar" role="img" aria-label="Portrait photo of John Doe"></div>
      <h4>John Doe</h4><div class="role">Member</div>
      <svg class="quote-mark" viewBox="0 0 18 14"><path d="M0 14V8C0 3 2 0 7 0v3C4 3 3 5 3 7h4v7zM11 14V8c0-5 2-8 7-8v3c-3 0-4 2-4 4h4v7z"/></svg>
      <p>The private events are the best part. I have met partners and friends I would never have crossed paths with anywhere else in town.</p>
    </div>
    <div class="person">
      <div class="avatar" role="img" aria-label="Portrait photo of John Smith"></div>
      <h4>John Smith</h4><div class="role">Member</div>
      <svg class="quote-mark" viewBox="0 0 18 14"><path d="M0 14V8C0 3 2 0 7 0v3C4 3 3 5 3 7h4v7zM11 14V8c0-5 2-8 7-8v3c-3 0-4 2-4 4h4v7z"/></svg>
      <p>From advisers to travel, one call does it all. Membership has given me back time, which is the one thing I could never buy before.</p>
    </div>
  </div>
</section>

<footer class="site-footer">
  <div class="band-photo" role="img" aria-label="Photo of a concert crowd under purple lights"></div>
  <div class="band-shade"></div>
  <div class="foot-brand">VORLEN</div>
  <p class="foot-about">A private lifestyle club offering travel, events and concierge services to members nationwide.</p>
  <div class="col col-contact">
    <h4>CONTACT US</h4>
    <div class="info">
      <svg width="18" height="22" viewBox="0 0 18 22"><path d="M9 0a8 8 0 0 0-8 8c0 6 8 14 8 14s8-8 8-14a8 8 0 0 0-8-8zm0 11a3 3 0 1 1 0-6 3 3 0 0 1 0 6z" fill="#fff"/></svg>
      <div><b>ADDRESS</b><br>118 Larkfield Row<br>Westbrook, Oregon 97000</div>
    </div>
    <div class="info">
      <svg width="18" height="18" viewBox="0 0 18 18"><path d="M4 1l3 4-2 2c1 2 3 4 6 6l2-2 4 3-2 3C8 17 1 10 1 3z" fill="#fff"/></svg>
      <div><b>PHONE NUMBER</b><br>1-555-014-2290</div>
    </div>
  </div>
  <div class="col col-about">
    <h4>ABOUT</h4>
    <a href="#">Home</a><a href="#">About Us</a><a href="#">Services/Benefits</a><a href="#">Contact Us</a>
  </div>
  <div class="col col-touch">
    <h4>GET IN TOUCH</h4>
    <div class="row"><div class="in" style="flex:1">Name</div><div class="in" style="flex:1">Phone</div></div>
    <div class="in">Email address</div>
    <a class="btn btn-light" href="#">SEND</a>
  </div>
  <div class="copyright">© 2018 VORLEN All Right Reserved</div>
</footer>

</body>
</html>
```